New Corporate website more focused on funnel and great design

Our company, Bold Harbor needs a new website to look like it's from 2021. We work with large businesses in the corporte world and need to reflect that we are professional, focused on our clients, and trsutworthy. It should include some/most of the components from our current site: boldharbor.com but should focus more about getting people to optin to out free downloads, which can be found on this page: https://www.boldharbor.com/get-started-with-a-prep-session/ and this page: https://www.boldharbor.com/team-onboarding/

Our new website should do a better job at explaining what we do, who we serve, and how we fix their problems of onboarding new leaders. Feel free to use dummy text if you are not sure what to put in for certain sections. I also would like to point out that most of the audiance is older, so we don't need anything too younge and flashy, or that is hard it use. it should have big clear fonts, plently of contrast, and work well for poeple who are not good at using the internet. Please use the colors of the logo, and you can add another color or two if you think it's fits

Industry/Entity Type

business consulting

Number of Pages Required

2 page

Font styles to use
Sans Serif

Requirements
Must have
• corporate feel, look professional, focus on getting new leads
Should not have
• cute or children feel

```html
<!DOCTYPE html>
<html lang="en">
<head>
<meta charset="utf-8">
<title>Bold Harbor — Leadership Transitions</title>
<link href="https://fonts.googleapis.com/css2?family=Roboto:ital,wght@0,400;0,500;0,700;1,400&display=swap" rel="stylesheet">
<style>
:root{
  --navy:#174a8b;
  --navy-dark:#123d74;
  --ink:#1b1b1b;
  --body:#3a3a3a;
  --muted:#6b6b6b;
  --charcoal:#2f3134;
  --footer:#1a1a1a;
  --line:#d9d9d9;
  --white:#ffffff;
  --tile:#f1f1f1;
}
*{margin:0;padding:0;box-sizing:border-box}
html,body{width:1200px;height:4955px;overflow:hidden}
body{font-family:'Roboto',Arial,sans-serif;color:var(--body);background:var(--white);position:relative}
.abs{position:absolute}
a{color:inherit;text-decoration:none}

/* top bar */
.topbar{top:0;left:0;width:1200px;height:38px;background:var(--navy)}
.topbar .social{left:100px;top:13px;display:flex;gap:14px}
.topbar .social span{width:12px;height:12px;border-radius:50%;background:var(--white);opacity:.9;display:block}
.topbar .phones{right:100px;top:11px;color:var(--white);font-size:13px;display:flex;gap:26px}
.phones svg,.contact-list svg{vertical-align:-2px;margin-right:6px}

/* nav */
.nav{top:38px;left:0;width:1200px;height:62px;background:var(--white)}
.brand{left:100px;top:17px;display:flex;align-items:center;gap:10px}
.brand-mark{width:28px;height:28px;background:var(--navy)}
.brand-name{font-size:24px;font-weight:500;color:var(--navy)}
.menu{left:366px;top:22px;display:flex;gap:30px;font-size:14px;font-weight:500;color:var(--ink)}
.menu .active{color:var(--navy)}
.menu .dd::after{content:"";display:inline-block;width:5px;height:5px;border-right:1.5px solid var(--ink);border-bottom:1.5px solid var(--ink);transform:rotate(45deg);margin-left:6px;vertical-align:3px}

/* hero */
.hero{top:100px;left:0;width:1200px;height:612px;background:linear-gradient(90deg,#4b5258 0%,#8a9096 45%,#c9ccce 100%)}
.hero-shade{top:100px;left:0;width:700px;height:612px;background:linear-gradient(90deg,rgba(20,24,30,.55),rgba(20,24,30,0))}
.hero h1{left:100px;top:362px;width:520px;font-size:45px;line-height:43px;font-weight:700;color:var(--white)}
.btn{display:flex;align-items:center;justify-content:center;background:var(--navy-dark);color:var(--white);font-weight:700;font-size:14px;border-radius:22px;letter-spacing:.3px}
.hero .btn{left:108px;top:550px;width:180px;height:40px}
.dots{left:558px;top:668px;display:flex;gap:12px}
.dots span{width:11px;height:11px;border-radius:50%;border:1.5px solid var(--white)}
.dots .on{background:var(--white)}

/* who we are */
.frame-line{background:var(--navy)}
.photo{display:block}
.eyebrow{font-size:15px;font-weight:500;color:var(--navy);letter-spacing:.3px}
.h2{font-size:33px;line-height:33px;font-weight:700;color:var(--ink)}
.copy{font-size:13.5px;line-height:25.5px;color:var(--body)}

/* section titles */
.section-title{left:0;width:1200px;text-align:center;font-size:38px;font-weight:700;color:var(--ink)}
.section-sub{left:0;width:1200px;text-align:center;font-size:16px;color:var(--ink)}

/* services */
.service{top:1427px;width:400px;height:423px;color:var(--white);padding:0 26px}
.service.dark{background:linear-gradient(160deg,#3b3d40,#232427)}
.service.blue{background:linear-gradient(160deg,#1f59a1,#123f78)}
.service svg{position:absolute;left:26px;top:54px}
.service h3{position:absolute;left:26px;top:158px;font-size:24px;font-weight:500;letter-spacing:.2px}
.service p{position:absolute;left:26px;top:206px;width:350px;font-size:13.5px;line-height:27px}
.service .more{position:absolute;left:26px;top:354px;font-size:14px;font-weight:700;display:flex;align-items:center;gap:8px}

/* how it works */
.step{left:100px;width:480px;height:100px}
.step .badge{position:absolute;left:0;top:0;width:85px;height:85px;border-radius:50%;background:var(--navy);display:flex;align-items:center;justify-content:center}
.step h4{position:absolute;left:98px;top:4px;font-size:20px;font-weight:500;color:var(--ink)}
.step p{position:absolute;left:98px;top:32px;width:370px;font-size:12px;line-height:22px;color:var(--body)}

/* who we serve */
.serve-card{top:2531px;width:323px;height:334px}
.serve-card .img{position:absolute;left:0;top:0;width:323px;height:280px}
.serve-card .label{position:absolute;left:0;top:280px;width:323px;height:54px;background:var(--navy);color:var(--white);font-size:21px;font-weight:500;display:flex;align-items:center;justify-content:center}

/* testimonial */
.quote-panel{top:2956px;left:602px;width:598px;height:534px;background:var(--navy);color:var(--white)}
.quote-panel .eyebrow{position:absolute;left:48px;top:55px;color:var(--white);font-size:13px}
.quote-panel h2{position:absolute;left:48px;top:80px;font-size:38px;font-weight:500;letter-spacing:.2px}
.quote-panel blockquote{position:absolute;left:48px;top:136px;width:480px;font-size:14.5px;line-height:28.5px;font-style:italic}
.partner{position:absolute;left:48px;top:318px;display:flex;align-items:center;gap:8px;font-size:17px}
.partner i{display:block;width:22px;height:22px;background:var(--white)}
.quote-panel .who{position:absolute;left:48px;top:367px;font-size:17px;font-weight:500}
.quote-panel .role{position:absolute;left:48px;top:395px;font-size:11.5px}
.arrows{position:absolute;left:48px;top:432px;display:flex;gap:11px}
.arrows span{width:27px;height:27px;border-radius:50%;border:1.5px solid var(--white);display:flex;align-items:center;justify-content:center}

/* blog */
.post{top:3632px;width:323px;height:387px}
.post .img{position:absolute;left:0;top:0;width:323px;height:233px}
.post .box{position:absolute;left:12px;top:181px;width:299px;height:206px;background:var(--white);box-shadow:0 2px 10px rgba(0,0,0,.12);text-align:center;padding:0 20px}
.post .date{margin-top:33px;font-size:13px;font-weight:500;color:var(--navy)}
.post h3{margin-top:10px;font-size:15px;line-height:22px;font-weight:500;color:var(--ink)}
.post p{margin-top:10px;font-size:11.5px;line-height:21px;color:var(--muted)}

/* clients */
.logo-tile{width:188px;height:92px;background:var(--tile);display:flex;align-items:center;justify-content:center;font-size:22px;font-weight:500;color:#4a4a4a}

/* footer */
.footer{top:4538px;left:0;width:1200px;height:417px;background:var(--footer);color:var(--white)}
.footer h5{position:absolute;font-size:20px;font-weight:500;letter-spacing:.2px}
.field{position:absolute;height:39px;border:1px solid #8a8a8a;background:var(--white);color:var(--ink);font-size:12.5px;padding:0 10px;display:flex;align-items:center}
.footer .send{position:absolute;left:100px;top:259px;width:446px;height:39px;background:var(--navy);font-size:13px;font-weight:500;display:flex;align-items:center;justify-content:center}
.contact-list{position:absolute;left:660px;top:120px;font-size:14.5px;line-height:32px}
.fsocial{position:absolute;left:660px;top:225px;display:flex;gap:9px}
.fsocial span{width:29px;height:29px;border-radius:50%;border:1.5px solid var(--white)}
.links{position:absolute;left:971px;top:120px;font-size:14.5px;line-height:32px}
.footer .rule{position:absolute;left:100px;top:346px;width:1000px;height:1px;background:#3a3a3a}
.footer .copyright{position:absolute;left:0;top:374px;width:1200px;text-align:center;font-size:13px}
</style>
</head>
<body>

<!-- top bar -->
<div class="abs topbar">
  <div class="abs social" aria-label="Social profiles"><span></span><span></span><span></span><span></span></div>
  <div class="abs phones">
    <span><svg width="12" height="12" viewBox="0 0 24 24" fill="#fff"><path d="M6.6 10.8a15.1 15.1 0 0 0 6.6 6.6l2.2-2.2c.3-.3.7-.4 1-.2 1.1.4 2.3.6 3.6.6.6 0 1 .4 1 1V20c0 .6-.4 1-1 1A17 17 0 0 1 3 4c0-.6.4-1 1-1h3.5c.6 0 1 .4 1 1 0 1.3.2 2.5.6 3.6.1.3 0 .7-.2 1z"/></svg>US +1 555.010.2040</span>
    <span><svg width="12" height="12" viewBox="0 0 24 24" fill="#fff"><path d="M6.6 10.8a15.1 15.1 0 0 0 6.6 6.6l2.2-2.2c.3-.3.7-.4 1-.2 1.1.4 2.3.6 3.6.6.6 0 1 .4 1 1V20c0 .6-.4 1-1 1A17 17 0 0 1 3 4c0-.6.4-1 1-1h3.5c.6 0 1 .4 1 1 0 1.3.2 2.5.6 3.6.1.3 0 .7-.2 1z"/></svg>UK +44 (0) 7700 900418</span>
  </div>
</div>

<!-- navigation -->
<div class="abs nav">
  <div class="abs brand"><span class="brand-mark"></span><span class="brand-name">Bold Harbor</span></div>
  <nav class="abs menu">
    <a class="active">HOME</a><a class="dd">WHO WE ARE</a><a class="dd">WHAT WE DO</a><a class="dd">CLIENTS</a><a>BLOG</a><a class="dd">RESOURCES</a><a>CONTACT</a>
  </nav>
</div>

<!-- hero -->
<div class="abs hero" role="img" aria-label="Photo of a group of business executives meeting around a laptop in a bright office"></div>
<div class="abs hero-shade"></div>
<h1 class="abs" style="left:100px;top:362px;width:520px;font-size:45px;line-height:43px;font-weight:700;color:#fff">Accelerate Business Performance During Critical Leadership Transitions</h1>
<a class="abs btn" style="left:108px;top:550px;width:180px;height:40px">GET STARTED</a>
<div class="abs dots"><span></span><span></span><span class="on"></span><span></span></div>

<!-- who we are -->
<div class="abs frame-line" style="left:345px;top:804px;width:236px;height:3px"></div>
<div class="abs frame-line" style="left:578px;top:804px;width:3px;height:270px"></div>
<div class="abs frame-line" style="left:100px;top:904px;width:3px;height:320px"></div>
<div class="abs frame-line" style="left:100px;top:1221px;width:248px;height:3px"></div>
<div class="abs photo" style="left:119px;top:823px;width:442px;height:381px;background:linear-gradient(135deg,#d8dde3,#a9b2bc 55%,#7c8692)" role="img" aria-label="Photo of a young executive and a senior colleague reviewing work on a laptop"></div>
<div class="abs eyebrow" style="left:636px;top:820px">WHO WE ARE</div>
<h2 class="abs h2" style="left:636px;top:852px;width:480px">TRANSITIONS ARE A CRUCIBLE OF LEADERSHIP</h2>
<p class="abs copy" style="left:636px;top:928px;width:460px">We know, through our personal experiences gained as leaders, that the first 100 days in a critical transition are a crucible of leadership – when managed well, leaders build cohesive teams that succeed. When managed poorly, leaders falter, teams stall, and organizations fail.</p>
<p class="abs copy" style="left:636px;top:1036px;width:460px">These experiences, and our motivation to make things better for leaders during critical transitions, became the initial catalyst for the creation of the tools that became the core of the Bold Harbor approach to our executive onboarding services and the foundation</p>
<a class="abs btn" style="left:636px;top:1160px;width:179px;height:44px">LEARN MORE</a>

<!-- what we do -->
<h2 class="abs section-title" style="top:1308px">WHAT WE DO</h2>
<p class="abs section-sub" style="top:1367px">Get done in 100 days what normally takes 6-12 months 90% of Bold Harbor clients succeed</p>

<div class="abs service dark" style="left:0">
  <svg width="70" height="76" viewBox="0 0 70 76" fill="none" stroke="#fff" stroke-width="2"><circle cx="35" cy="20" r="9"/><path d="M20 52c0-10 7-17 15-17s15 7 15 17"/><circle cx="12" cy="36" r="6"/><circle cx="58" cy="36" r="6"/><path d="M2 62c0-8 4-13 10-13s10 5 10 13M48 62c0-8 4-13 10-13s10 5 10 13M2 72h66"/></svg>
  <h3>EXECUTIVE ONBOARDING</h3>
  <p>40% of new leaders fail For executive leaders taking on new roles, the Bold Harbor 100-Day Action Plan process prepares leaders before the start, speeds up assimilation, sets direction, builds the team, accelerates momentum, and delivers results.</p>
  <a class="more">LEARN MORE <svg width="14" height="14" viewBox="0 0 14 14"><circle cx="7" cy="7" r="7" fill="#fff"/><path d="M5.5 4l3 3-3 3" stroke="#2f3134" stroke-width="1.8" fill="none"/></svg></a>
</div>
<div class="abs service blue" style="left:400px">
  <svg width="76" height="76" viewBox="0 0 76 76" fill="none" stroke="#fff" stroke-width="2"><circle cx="38" cy="26" r="20"/><circle cx="38" cy="26" r="8"/><path d="M8 52l14 10 10-6 6 6 6-6 10 6 14-10M22 62l8 8M44 62l-6 8"/></svg>
  <h3>TEAM ONBOARDING</h3>
  <p>80% of M&amp;A fail to boost returns For leaders integrating teams post acquisition or re-organization, the Bold Harbor 100 Day Action Plan process gets all players on board with the change and accelerates achievement of cultural and business</p>
  <a class="more">LEARN MORE <svg width="14" height="14" viewBox="0 0 14 14"><circle cx="7" cy="7" r="7" fill="#fff"/><path d="M5.5 4l3 3-3 3" stroke="#174a8b" stroke-width="1.8" fill="none"/></svg></a>
</div>
<div class="abs service dark" style="left:800px">
  <svg width="80" height="76" viewBox="0 0 80 76" fill="none" stroke="#fff" stroke-width="2"><rect x="4" y="6" width="62" height="46"/><path d="M14 42V32M24 42V24M34 42V28M14 20l10-6 10 4 12-8"/><circle cx="54" cy="44" r="10"/><path d="M61 51l12 12M20 52l-6 18M50 52l6 18"/></svg>
  <h3>ACCELERATION &amp; RESTART</h3>
  <p>70% of transformations fall short For executives leading through a strategic point of inflection or reinvigorating a stalled team, Bold Harbor programs define the from-to challenge, kickstart a change process and deliver results that stick.</p>
  <a class="more">LEARN MORE <svg width="14" height="14" viewBox="0 0 14 14"><circle cx="7" cy="7" r="7" fill="#fff"/><path d="M5.5 4l3 3-3 3" stroke="#2f3134" stroke-width="1.8" fill="none"/></svg></a>
</div>

<!-- how it works -->
<div class="abs eyebrow" style="left:100px;top:1942px">HOW IT WORK</div>
<h2 class="abs h2" style="left:100px;top:1970px;width:500px;font-size:31px;line-height:34px">HOW WE FIX THEIR PROBLEMS OF ONBOARDING NEW LEADERS.</h2>

<div class="abs step" style="top:2057px">
  <div class="badge"><svg width="42" height="42" viewBox="0 0 42 42" fill="none" stroke="#fff" stroke-width="2"><circle cx="21" cy="12" r="6"/><path d="M10 34c0-7 5-12 11-12s11 5 11 12"/><circle cx="6" cy="22" r="3"/><circle cx="36" cy="22" r="3"/></svg></div>
  <h4>Finibus Bonorum et Malorum</h4>
  <p>Lorem ipsum dolor sit amet, consectetur adipiscing elit, so eiusmod tempor incididunt ut labore et dolore magiqua. Quis im suspendisse ultrices gravida.</p>
</div>
<div class="abs step" style="top:2171px">
  <div class="badge"><svg width="42" height="42" viewBox="0 0 42 42" fill="none" stroke="#fff" stroke-width="2"><rect x="4" y="5" width="14" height="12"/><rect x="24" y="5" width="14" height="12"/><circle cx="11" cy="30" r="6"/><circle cx="31" cy="30" r="6"/><path d="M18 11h6M11 17v7M31 17v7"/></svg></div>
  <h4>Finibus Bonorum et Malorum</h4>
  <p>Lorem ipsum dolor sit amet, consectetur adipiscing elit, so eiusmod tempor incididunt ut labore et dolore magiqua. Quis im suspendisse ultrices gravida.</p>
</div>
<div class="abs step" style="top:2284px">
  <div class="badge"><svg width="42" height="42" viewBox="0 0 42 42" fill="none" stroke="#fff" stroke-width="2"><circle cx="18" cy="12" r="6"/><path d="M6 36c0-8 5-14 12-14 4 0 7 2 9 5"/><circle cx="31" cy="30" r="7"/><path d="M28 30l2 2 4-4"/></svg></div>
  <h4>Finibus Bonorum et Malorum</h4>
  <p>Lorem ipsum dolor sit amet, consectetur adipiscing elit, so eiusmod tempor incididunt ut labore et dolore magiqua. Quis im suspendisse ultrices gravida.</p>
</div>

<div class="abs frame-line" style="left:619px;top:1944px;width:3px;height:190px"></div>
<div class="abs frame-line" style="left:619px;top:1944px;width:150px;height:3px"></div>
<div class="abs frame-line" style="left:1096px;top:2170px;width:3px;height:195px"></div>
<div class="abs frame-line" style="left:948px;top:2362px;width:151px;height:3px"></div>
<div class="abs photo" style="left:638px;top:1963px;width:441px;height:383px;background:linear-gradient(135deg,#9aa59f,#6d7a78 50%,#3f4a4d)" role="img" aria-label="Photo of a senior mentor and a younger leader reviewing notes at a laptop"></div>

<!-- who we serve -->
<h2 class="abs section-title" style="top:2458px">WHO WE SERVE</h2>
<div class="abs serve-card" style="left:100px"><div class="img" style="background:linear-gradient(135deg,#c9c2b5,#8d8478 60%,#5b554f)" role="img" aria-label="Photo of executives in discussion at a conference table"></div><div class="label">THE STANDARD LOREM</div></div>
<div class="abs serve-card" style="left:438px"><div class="img" style="background:linear-gradient(135deg,#eceae6,#b9b6b0 55%,#5e5c5a)" role="img" aria-label="Photo of a presenter at a flip chart addressing a seated team"></div><div class="label">THE STANDARD LOREM</div></div>
<div class="abs serve-card" style="left:777px"><div class="img" style="background:linear-gradient(135deg,#a7b3bb,#6f7b84 55%,#3e474e)" role="img" aria-label="Photo of business partners reviewing documents together"></div><div class="label">THE STANDARD LOREM</div></div>

<!-- testimonial -->
<div class="abs" style="left:0;top:2956px;width:602px;height:534px;background:linear-gradient(120deg,#b7bcc0,#d7d8d6 50%,#9ea4a9)" role="img" aria-label="Photo of a smiling businesswoman holding a tablet outside an office building"></div>
<div class="abs quote-panel">
  <div class="eyebrow">TESTMONIALS</div>
  <h2>WHAT OUR CLIENTS SAY</h2>
  <blockquote>"I have worked with Bold Harbor twice in the last 24 months, first as a private equity investor and most recently as a first time leader of a company. In both cases, their process and facilitation created nearly immediate alignment around our strategy and tactics that dramatically accelerated value creation...We accomplished nearly a year of positive change within a month"</blockquote>
  <div class="partner"><i></i>Northvale Partners</div>
  <div class="who">- Daniel Brooks</div>
  <div class="role">Former Managing Director of Northvale Private Equity Firm</div>
  <div class="arrows">
    <span><svg width="10" height="10" viewBox="0 0 10 10"><path d="M6.5 1.5L3 5l3.5 3.5" stroke="#fff" stroke-width="1.6" fill="none"/></svg></span>
    <span><svg width="10" height="10" viewBox="0 0 10 10"><path d="M3.5 1.5L7 5 3.5 8.5" stroke="#fff" stroke-width="1.6" fill="none"/></svg></span>
  </div>
</div>

<!-- featured posts -->
<h2 class="abs section-title" style="top:3557px">FEATURED BOOKS &amp; BLOG POSTS</h2>
<article class="abs post" style="left:100px">
  <div class="img" style="background:linear-gradient(135deg,#d2d2d2,#8f8f8f 60%,#555)" role="img" aria-label="Black and white archival photo of two gentlemen in suits"></div>
  <div class="box"><div class="date">📅 Jul 27, 2021</div><h3>WHY 'THANK YOU' BEATS 'YES' IN STRATEGIC SELLING</h3><p>Strategic selling is about collaboratively finding ways to solve others' problems. This is materially different than convincing prospects</p></div>
</article>
<article class="abs post" style="left:438px">
  <div class="img" style="background:linear-gradient(135deg,#6c6a66,#3e3c39 55%,#242321)" role="img" aria-label="Photo of executives seated at a hearing table with microphones"></div>
  <div class="box"><div class="date">📅 Jul 27, 2021</div><h3>WHY CORVANE'S NEW CFO SHOULD FAIL, BUT WON'T</h3><p>40% of new leaders fail in their first 18 months. Witness Corvane's new CFO, Karen Miles who lasted less than 15 months</p></div>
</article>
<article class="abs post" style="left:777px">
  <div class="img" style="background:linear-gradient(135deg,#1b1b1b,#3a3631 50%,#121212)" role="img" aria-label="Photo of a framed bottle print lit in a dark room"></div>
  <div class="box"><div class="date">📅 Jul 27, 2021</div><h3>WHEN TO INFORM IN ADVANCE VERSUS REPORT AFTER</h3><p>What does "Keep me informed" mean? Figure it out by asking "Before or after?" Most people won't know what you mean</p></div>
</article>

<!-- clients -->
<h2 class="abs section-title" style="top:4182px;font-size:28px;font-weight:500">OUR TOP 10 CLIENTS HAVE USED US OVER 180 TIMES</h2>
<div class="abs logo-tile" style="left:100px;top:4246px">Altaris</div>
<div class="abs logo-tile" style="left:304px;top:4246px">Mara Lane</div>
<div class="abs logo-tile" style="left:507px;top:4246px">Ironwell</div>
<div class="abs logo-tile" style="left:710px;top:4246px">Atrelle</div>
<div class="abs logo-tile" style="left:912px;top:4246px">Ashgrove</div>
<div class="abs logo-tile" style="left:100px;top:4350px">Axiline</div>
<div class="abs logo-tile" style="left:304px;top:4350px">Bluvera</div>
<div class="abs logo-tile" style="left:507px;top:4350px">Barlow's</div>
<div class="abs logo-tile" style="left:710px;top:4350px">Brook &amp; Fenn</div>
<div class="abs logo-tile" style="left:912px;top:4350px">Camlen</div>

<!-- footer -->
<footer class="abs footer">
  <h5 style="left:100px;top:78px">SPEAK TO ONE OF OUR PARTNERS TODAY</h5>
  <div class="field" style="left:100px;top:117px;width:219px">First Name</div>
  <div class="field" style="left:327px;top:117px;width:219px">Last Name</div>
  <div class="field" style="left:100px;top:165px;width:219px">Email</div>
  <div class="field" style="left:327px;top:165px;width:219px">Phone</div>
  <div class="field" style="left:100px;top:212px;width:446px">Message</div>
  <div class="send">SPEAK TO A PARTNER TODAY</div>

  <h5 style="left:660px;top:78px">CONTACT INFO</h5>
  <div class="contact-list">
    <div><svg width="13" height="13" viewBox="0 0 24 24" fill="#fff"><path d="M6.6 10.8a15.1 15.1 0 0 0 6.6 6.6l2.2-2.2c.3-.3.7-.4 1-.2 1.1.4 2.3.6 3.6.6.6 0 1 .4 1 1V20c0 .6-.4 1-1 1A17 17 0 0 1 3 4c0-.6.4-1 1-1h3.5c.6 0 1 .4 1 1 0 1.3.2 2.5.6 3.6.1.3 0 .7-.2 1z"/></svg>US +1 555.010.2040</div>
    <div><svg width="13" height="13" viewBox="0 0 24 24" fill="#fff"><path d="M6.6 10.8a15.1 15.1 0 0 0 6.6 6.6l2.2-2.2c.3-.3.7-.4 1-.2 1.1.4 2.3.6 3.6.6.6 0 1 .4 1 1V20c0 .6-.4 1-1 1A17 17 0 0 1 3 4c0-.6.4-1 1-1h3.5c.6 0 1 .4 1 1 0 1.3.2 2.5.6 3.6.1.3 0 .7-.2 1z"/></svg>UK +44 (0) 7700 900418</div>
    <div><svg width="13" height="13" viewBox="0 0 24 24" fill="#fff"><path d="M2 5h20v14H2z M2 5l10 8 10-8" stroke="#1a1a1a" stroke-width="1.5"/></svg>inquiry@boldharbor.com</div>
  </div>
  <div class="fsocial" aria-label="Social profiles"><span></span><span></span><span></span><span></span></div>

  <h5 style="left:971px;top:78px">QUICK LINKS</h5>
  <div class="links"><div>Who We Are</div><div>What We Do</div><div>Clients</div><div>Blog</div><div>Resources</div><div>Contact</div></div>

  <div class="rule"></div>
  <div class="copyright">©Copyright ©2021 Bold Harbor . All Rights Reserved.</div>
</footer>

</body>
</html>
```